Hollowbrook Renderworks plain circle mark Design

I would like a design for my friends company. He has just had his logo designed and really likes the following website.

www.tbr-skimcoat.co.uk

Something similar to this design would be ideal but open to additional ideas. The website shown has all the relevant content.

We have 20 years of experience and can provide a number of photos for work we have done.

More photos will be provided upon request.

Target Market(s)

Homeowners

Industry/Entity Type

Trade

Font styles to use
Sans Serif

Colors
3176b5
85cae6
85abd2
eaf1f7

Requirements
Must have
• look at www.tbr-skimcoat.co.uk
Nice to have
Should not have
• N/A

```html
<!DOCTYPE html>
<html lang="en">
<head>
<meta charset="utf-8">
<title>Hollowbrook Renderworks</title>
<link rel="stylesheet" href="https://fonts.googleapis.com/css2?family=Open+Sans:wght@400;600;700&family=Noto+Serif:wght@700&display=swap">
<style>
  :root {
    --admin-bar: #23282d;
    --admin-text: #eeeeee;
    --admin-icon: #a0a5aa;
    --brand-blue: #3176b5;
    --brand-sky: #85cae6;
    --brand-soft: #85abd2;
    --brand-pale: #eaf1f7;
    --nav-text: #555b61;
    --nav-rule: #d5d9dd;
    --white: #ffffff;
    --field-border: #cfcfcf;
    --placeholder: #8a8f94;
    --hero-sky: #7fb3e6;
    --hero-timber: #2a2d33;
    --hero-wall: #d9d6cf;
    --figure-tone: #5a6478;
  }
  * { box-sizing: border-box; margin: 0; padding: 0; }
  html, body { width: 1200px; height: 590px; overflow: hidden; background: var(--white); }
  body { position: relative; font-family: "Open Sans", Arial, sans-serif; }

  .admin-bar {
    position: absolute; left: 0; top: 0; width: 1200px; height: 24px;
    background: var(--admin-bar); color: var(--admin-text); font-size: 13px;
  }
  .admin-left { position: absolute; left: 12px; top: 0; height: 24px; display: flex; align-items: center; gap: 16px; }
  .admin-right { position: absolute; right: 10px; top: 0; height: 24px; display: flex; align-items: center; gap: 14px; }
  .admin-bar .item { display: flex; align-items: center; gap: 6px; white-space: nowrap; }
  .admin-bar svg { display: block; flex: none; }
  .admin-bar .muted { color: var(--admin-icon); }
  .admin-bar .avatar { width: 16px; height: 16px; background: #c9c9c9; display: inline-block; }

  .top-strip {
    position: absolute; left: 5px; top: 24px; width: 1185px; height: 31px;
    background: var(--brand-blue); color: var(--white); font-size: 13px;
    display: flex; align-items: center; gap: 22px; padding-left: 96px;
  }

  .site-header { position: absolute; left: 5px; top: 55px; width: 1185px; height: 84px; background: var(--white); }
  .brand { position: absolute; left: 95px; top: 24px; display: flex; align-items: center; gap: 8px; }
  .brand-square { width: 14px; height: 14px; background: var(--brand-blue); }
  .brand-name { font-size: 17px; font-weight: 600; color: var(--brand-blue); letter-spacing: 0.3px; }

  .main-nav { position: absolute; right: 84px; top: 30px; display: flex; font-size: 14px; color: var(--nav-text); }
  .main-nav a { color: inherit; text-decoration: none; padding: 2px 7px; border-left: 1px solid var(--nav-rule); line-height: 20px; }
  .main-nav a:first-child { border-left: none; }
  .main-nav a.current { color: var(--brand-blue); }

  .hero { position: absolute; left: 5px; top: 139px; width: 1185px; height: 451px; overflow: hidden; }
  .hero-photo {
    position: absolute; inset: 0;
    background:
      linear-gradient(180deg, rgba(0,0,0,0) 60%, rgba(0,0,0,0.35) 100%),
      linear-gradient(100deg, var(--hero-timber) 0%, #4a4a4e 18%, var(--hero-wall) 40%, var(--hero-sky) 62%, #9fc4ea 78%, #5d5c60 100%);
  }
  .hero-title {
    position: absolute; left: 0; width: 1195px; top: 56px; text-align: center;
    font-family: "Noto Serif", Georgia, serif; font-weight: 700; font-size: 30px; color: var(--white);
    text-shadow: 0 1px 3px rgba(0,0,0,0.4);
  }
  .quote-form .field {
    position: absolute; left: 171px; width: 269px; height: 37px;
    background: var(--white); border: 1px solid var(--field-border); border-radius: 2px;
    font-size: 12px; color: var(--placeholder); padding: 10px 10px;
  }
  .check-box {
    position: absolute; left: 171px; top: 283px; width: 285px; height: 71px;
    background: #f9f9f9; border: 1px solid #d3d3d3; border-radius: 3px; box-shadow: 0 0 4px rgba(0,0,0,0.1);
  }
  .check-box .tick { position: absolute; left: 12px; top: 23px; width: 26px; height: 26px; border: 2px solid #c1c1c1; border-radius: 2px; background: var(--white); }
  .check-box .label { position: absolute; left: 50px; top: 25px; font-size: 13px; color: #222; }
  .check-box .badge { position: absolute; left: 232px; top: 10px; width: 28px; height: 28px; border-radius: 50%; background: var(--brand-soft); }
  .check-box .badge-name { position: absolute; left: 210px; top: 42px; font-size: 8px; color: #555; width: 70px; text-align: center; }
  .check-box .badge-links { position: absolute; left: 210px; top: 55px; font-size: 7px; color: #555; width: 70px; text-align: center; }

  .contact-button {
    position: absolute; left: 171px; top: 371px; width: 100px; height: 41px;
    background: var(--brand-blue); color: var(--white); font-size: 13px; font-weight: 700;
    display: flex; align-items: center; justify-content: center;
  }
  .call-line { position: absolute; left: 295px; top: 378px; font-size: 17px; font-weight: 700; color: var(--white); text-shadow: 0 1px 2px rgba(0,0,0,0.5); }

  .worker-photo {
    position: absolute; left: 785px; top: 108px; width: 160px; height: 325px;
    background: linear-gradient(180deg, #7c879b 0%, var(--figure-tone) 100%);
    opacity: 0.85; border-radius: 4px;
  }
</style>
</head>
<body>
  <div class="admin-bar">
    <div class="admin-left">
      <div class="item"><svg width="18" height="18" viewBox="0 0 18 18"><circle cx="9" cy="9" r="8" fill="#a0a5aa"/></svg></div>
      <div class="item"><svg width="16" height="16" viewBox="0 0 16 16"><path d="M2 14 A6 6 0 0 1 14 14 Z" fill="#a0a5aa"/><circle cx="8" cy="6" r="4" fill="#a0a5aa"/></svg><span>Hollowbrook Renderworks</span></div>
      <div class="item"><svg width="16" height="16" viewBox="0 0 16 16"><path d="M2 14 L11 5 L13 7 L4 16 Z" fill="#a0a5aa"/><path d="M11 2 L14 5" stroke="#a0a5aa" stroke-width="2"/></svg><span>Customize</span></div>
      <div class="item"><svg width="16" height="16" viewBox="0 0 16 16"><path d="M3 8 A5 5 0 0 1 13 6 M13 8 A5 5 0 0 1 3 10" stroke="#a0a5aa" stroke-width="2" fill="none"/></svg><span>2</span></div>
      <div class="item"><svg width="16" height="16" viewBox="0 0 16 16"><path d="M2 2 H14 V11 H6 L3 14 V11 H2 Z" fill="#a0a5aa"/></svg><span class="muted">0</span></div>
      <div class="item"><svg width="14" height="14" viewBox="0 0 14 14"><path d="M7 1 V13 M1 7 H13" stroke="#a0a5aa" stroke-width="2.5"/></svg><span>New</span></div>
      <div class="item"><svg width="16" height="16" viewBox="0 0 16 16"><path d="M3 13 L4 9 L11 2 L14 5 L7 12 Z" stroke="#a0a5aa" stroke-width="1.5" fill="none"/></svg><span>Edit Page</span></div>
    </div>
    <div class="admin-right">
      <div class="item"><span>Howdy, hollowbrook_renderworks</span><span class="avatar"></span></div>
      <div class="item"><svg width="15" height="15" viewBox="0 0 15 15"><circle cx="6" cy="6" r="4.5" stroke="#a0a5aa" stroke-width="2" fill="none"/><path d="M9.5 9.5 L14 14" stroke="#a0a5aa" stroke-width="2"/></svg></div>
    </div>
  </div>

  <div class="top-strip">
    <span>Have Any Questions?</span>
    <span>Call : 000-000-000</span>
    <span>Email: email@hollowbrookrenderworks.co.uk</span>
  </div>

  <header class="site-header">
    <div class="brand"><span class="brand-square"></span><span class="brand-name">Hollowbrook Renderworks</span></div>
    <nav class="main-nav">
      <a class="current">Home</a><a>About Us</a><a>Our Services</a><a>Contact Us</a>
    </nav>
  </header>

  <section class="hero">
    <div class="hero-photo" role="img" aria-label="Photo of a timber-framed house with pitched tiled roofs under a blue sky"></div>
    <h1 class="hero-title">Welcome to Hollowbrook Renderworks</h1>
    <form class="quote-form">
      <div class="field" style="top:118px">Your Name</div>
      <div class="field" style="top:173px">Your Email</div>
      <div class="field" style="top:229px">Your Contact No.</div>
      <div class="check-box">
        <span class="tick"></span>
        <span class="label">I'm not a robot</span>
        <span class="badge"></span>
        <span class="badge-name">HumanCheck</span>
        <span class="badge-links">Privacy - Terms</span>
      </div>
      <div class="contact-button">Contact Me</div>
    </form>
    <div class="call-line">or Call : 000-000-0000</div>
    <div class="worker-photo" role="img" aria-label="Photo of a smiling tradesman in work clothes with arms crossed"></div>
  </section>
</body>
</html>
```